Riverstone & Pine Construction and Developments business cards

A business card with watermark background (construction work)

Company logo attached

Home improvement projects
House renovations
Bathroom and kitchen renovations
House extensions
New builds and granny flats

Director Omar Haddine
(Phone number)
omar@rpcbuildgroup.com.au
(Instagram logo) rpc_buildgroup

```html
<!DOCTYPE html>
<html lang="en">
<head>
<meta charset="utf-8">
<title>Riverstone &amp; Pine Construction and Developments – Business Cards</title>
<link rel="stylesheet" href="https://fonts.googleapis.com/css2?family=Poppins:wght@400;600&family=Roboto:wght@400&display=swap">
<style>
  :root {
    --canvas: #e9e6e1;
    --card: #f7f7f7;
    --brand-blue: #2f79c0;
    --ink: #1d1d1d;
    --rule: #2f79c0;
    --wash: #dfe6f1;
  }
  * { box-sizing: border-box; margin: 0; padding: 0; }
  html, body { width: 900px; height: 1200px; overflow: hidden; }
  body { background: var(--canvas); position: relative; font-family: "Roboto", sans-serif; color: var(--ink); }

  .card {
    position: absolute;
    width: 773px;
    height: 448px;
    background: var(--card);
    border-radius: 20px;
    box-shadow: 0 6px 18px rgba(0,0,0,.18);
    overflow: hidden;
  }
  .card--front { left: 72px; top: 135px; }
  .card--back  { left: 74px; top: 625px;
    background: radial-gradient(ellipse at 50% 45%, var(--card) 35%, var(--wash) 100%); }

  .brand {
    position: absolute;
    display: flex;
    align-items: center;
    gap: 14px;
    color: var(--brand-blue);
    font-family: "Poppins", sans-serif;
    font-weight: 600;
    line-height: 1.15;
  }
  .brand__mark { width: 22px; height: 22px; background: var(--brand-blue); flex: none; }
  .card--front .brand { left: 48px; top: 135px; width: 320px; font-size: 26px; }
  .card--back  .brand { left: 200px; top: 140px; width: 380px; font-size: 32px; }

  .person { position: absolute; left: 401px; top: 86px; }
  .person__name { font-family: "Poppins", sans-serif; font-weight: 600; font-size: 31px; color: var(--brand-blue); line-height: 1.15; }
  .person__role { font-family: "Poppins", sans-serif; font-size: 22px; line-height: 1.1; }

  .contacts { position: absolute; left: 401px; top: 192px; list-style: none; }
  .contacts li { display: flex; align-items: center; gap: 10px; font-size: 19.5px; height: 38.5px; }
  .contacts svg { width: 26px; height: 20px; flex: none; fill: var(--brand-blue); }
  .social-box { width: 20px; height: 20px; margin: 0 3px; background: var(--brand-blue); border-radius: 4px; flex: none; }

  .services {
    position: absolute;
    border-top: 2px solid var(--rule);
    text-align: center;
    font-size: 19.5px;
    padding-top: 13px;
    word-spacing: 1px;
  }
  .card--front .services { left: 35px; right: 33px; top: 372px; }
  .card--back  .services { left: 43px; right: 29px; top: 370px; }
</style>
</head>
<body>

<section class="card card--front" aria-label="Business card front">
  <div class="brand">
    <span class="brand__mark"></span>
    <span>Riverstone &amp; Pine Construction and Developments</span>
  </div>

  <div class="person">
    <p class="person__name">Omar Haddine</p>
    <p class="person__role">Director</p>
  </div>

  <ul class="contacts">
    <li>
      <svg viewBox="0 0 26 20" aria-hidden="true"><path d="M2 7c0-3 5-5 11-5s11 2 11 5l-1 2-5-1V6c-3-1-7-1-10 0v2L3 9z"/><path d="M7 9h12l3 9H4z"/><circle cx="13" cy="13.5" r="2.5" fill="#f7f7f7"/></svg>
      123 456 7890
    </li>
    <li>
      <svg viewBox="0 0 26 20" aria-hidden="true"><rect x="2" y="3" width="22" height="15" fill="none" stroke="#2f79c0" stroke-width="2"/><path d="M2 3l11 9 11-9" fill="none" stroke="#2f79c0" stroke-width="2"/></svg>
      omar@rpcbuildgroup.com.au
    </li>
    <li>
      <span class="social-box" aria-hidden="true"></span>
      rpc_buildgroup
    </li>
  </ul>

  <p class="services">Home Improvement Projects &nbsp;|&nbsp; House Extensions &nbsp;|&nbsp; House Renovations</p>
</section>

<section class="card card--back" aria-label="Business card back">
  <div class="brand">
    <span class="brand__mark"></span>
    <span>Riverstone &amp; Pine Construction and Developments</span>
  </div>

  <p class="services">Bathroom and Kitchen Renovations &nbsp;|&nbsp; New Builds and Granny Flats</p>
</section>

</body>
</html>
```